New Business Card

We need to refresh our business cards. We designed these ourselves and we have no graphic design experience. We would like to find a new business card design that is professional and unique. We are an auto finance company. Feel free to play with the logo, but we would like to keep the eye very present on the card. Our corporate colors are green, grey, and white.
Green - RGB - 168,215,27; HEX - #AADD22
Grey - RGB - 196,196,196; HEX - #C4C4C4
Updates
Need to upload the vector file to finalize the project. The last logo was for a jpeg that didn't stretch well.
Industry/Entity Type
Financial Service
Contact Information for Business Card
Honestly don't know...I need your help!

```html
<!DOCTYPE html>
<html lang="en">
<head>
<meta charset="utf-8">
<title>Clearway Capital — Business Card</title>
<link href="https://fonts.googleapis.com/css2?family=Open+Sans:wght@400;600&family=Crimson+Text&display=swap" rel="stylesheet">
<style>
  :root {
    --lime: #7ff000;
    --lime-soft: #8cf51a;
    --charcoal: #5e5e5e;
    --mist: #c4cdcd;
    --ink: #2e2e2e;
    --tag-ink: #555555;
    --icon-bg: #111111;
    --paper: #ffffff;
  }
  html, body {
    margin: 0;
    padding: 0;
    width: 1200px;
    height: 720px;
    overflow: hidden;
    background: var(--paper);
  }
  .card {
    position: relative;
    width: 1200px;
    height: 720px;
    background: var(--paper);
    overflow: hidden;
  }
  .frame { position: absolute; }
  .frame--lime { left: 0; top: 0; width: 600px; height: 720px; background: var(--lime); }
  .frame--edge { left: 0; top: 41px; width: 39px; height: 679px; background: var(--charcoal); }
  .frame--panel { left: 81px; top: 41px; width: 1119px; height: 639px; background: var(--paper); }
  .frame--bar-top { left: 81px; top: 41px; width: 518px; height: 39px; background: var(--charcoal); }
  .frame--bar-bottom { left: 81px; top: 640px; width: 518px; height: 39px; background: var(--charcoal); }
  .frame--open { left: 600px; top: 0; width: 600px; height: 720px; background: var(--paper); }

  .side-tab {
    position: absolute;
    left: 1120px;
    top: 40px;
    width: 80px;
    height: 640px;
    border-radius: 54px 0 0 54px;
    background: repeating-linear-gradient(135deg, var(--lime) 0 3px, var(--lime-soft) 3px 6px);
  }

  .brand-dot {
    position: absolute;
    left: 178px;
    top: 108px;
    width: 268px;
    height: 268px;
    border-radius: 50%;
    background: var(--mist);
  }

  .brand-name {
    position: absolute;
    left: 578px;
    top: 153px;
    margin: 0;
    font-family: "Open Sans", sans-serif;
    font-weight: 600;
    line-height: 1;
  }
  .brand-name__main {
    display: block;
    font-size: 116px;
    letter-spacing: -2px;
    color: var(--lime);
  }
  .brand-name__sub {
    display: block;
    font-size: 50px;
    letter-spacing: 39px;
    margin-top: 38px;
    margin-left: 39px;
    color: var(--mist);
  }

  .tagline {
    position: absolute;
    left: 702px;
    top: 484px;
    margin: 0;
    font-family: "Crimson Text", serif;
    font-size: 42px;
    font-weight: 400;
    color: var(--tag-ink);
    letter-spacing: -0.5px;
  }

  .contact {
    position: absolute;
    left: 81px;
    top: 427px;
    margin: 0;
    padding: 0;
    list-style: none;
  }
  .contact__icons {
    position: absolute;
    left: 81px;
    top: 427px;
    width: 53px;
    height: 211px;
    background: var(--icon-bg);
    border-radius: 6px;
  }
  .contact__item {
    display: flex;
    align-items: center;
    height: 53px;
  }
  .contact__icon {
    width: 53px;
    height: 53px;
    display: flex;
    align-items: center;
    justify-content: center;
    flex: none;
  }
  .contact__icon svg { width: 22px; height: 22px; }
  .contact__text {
    margin-left: 29px;
    font-family: "Open Sans", sans-serif;
    font-size: 27px;
    color: var(--ink);
    letter-spacing: 0.2px;
  }
</style>
</head>
<body>
<main class="card">
  <div class="frame frame--lime"></div>
  <div class="frame frame--edge"></div>
  <div class="frame frame--panel"></div>
  <div class="frame frame--open"></div>
  <div class="frame frame--bar-top"></div>
  <div class="frame frame--bar-bottom"></div>

  <div class="side-tab"></div>

  <div class="brand-dot"></div>
  <h1 class="brand-name">
    <span class="brand-name__main">Clearway</span>
    <span class="brand-name__sub">CAPITAL</span>
  </h1>

  <p class="tagline">FINANCIAL SERVICE</p>

  <div class="contact__icons"></div>
  <ul class="contact">
    <li class="contact__item">
      <span class="contact__icon">
        <svg viewBox="0 0 24 24" fill="none" stroke="#fff" stroke-width="2" stroke-linecap="round" stroke-linejoin="round">
          <path d="M5 3h3l2 5-2.5 1.5a11 11 0 0 0 7 7L16 14l5 2v3a2 2 0 0 1-2 2A16 16 0 0 1 3 5a2 2 0 0 1 2-2z"/>
          <path d="M14 3a7 7 0 0 1 7 7"/>
          <path d="M14 7a3 3 0 0 1 3 3"/>
        </svg>
      </span>
      <span class="contact__text">+1 555 0148</span>
    </li>
    <li class="contact__item">
      <span class="contact__icon">
        <svg viewBox="0 0 24 24" fill="#fff">
          <path d="M2 5h20v14H2z"/>
          <path d="M2 5l10 8 10-8" fill="none" stroke="#111" stroke-width="1.6"/>
        </svg>
      </span>
      <span class="contact__text">info@clearway.com</span>
    </li>
    <li class="contact__item">
      <span class="contact__icon">
        <svg viewBox="0 0 24 24" fill="none" stroke="#fff" stroke-width="1.8">
          <circle cx="12" cy="12" r="9.5"/>
          <ellipse cx="12" cy="12" rx="4.2" ry="9.5"/>
          <path d="M2.5 12h19M4 7h16M4 17h16"/>
        </svg>
      </span>
      <span class="contact__text">www.clearway.com</span>
    </li>
    <li class="contact__item">
      <span class="contact__icon">
        <svg viewBox="0 0 24 24" fill="#fff">
          <path d="M12 2a7 7 0 0 0-7 7c0 5 7 13 7 13s7-8 7-13a7 7 0 0 0-7-7zm0 9.5A2.5 2.5 0 1 1 12 6.5a2.5 2.5 0 0 1 0 5z"/>
        </svg>
      </span>
      <span class="contact__text">12 Oak Street.</span>
    </li>
  </ul>
</main>
</body>
</html>
```